Real Estate Company
Residential & Commercial
Sales & Property Management

would like to use the logo i uploaded but would really love a black back ground...I think with the gold fleur dis lis and the maroon lettering it would really look great!

Industry/Entity Type

Business

Contact Information for Business Card

Bright Harbor Real Estate Co.
Renata Dubois
Broker/Owner
337-502-4173 Cell
337-618-9034 Office
4172 Pelton Rd Belle Ridge LA 70612

```html
<!DOCTYPE html>
<html lang="en">
<head>
<meta charset="utf-8">
<title>Bright Harbor Real Estate Co. — Business Card</title>
<link rel="stylesheet" href="https://fonts.googleapis.com/css2?family=Cinzel:wght@400;600;700&display=swap">
<style>
  :root {
    --stage: #3a3a3a;
    --card-black: #0b0b0b;
    --card-white: #fbfbfb;
    --gold-light: #f2dd8c;
    --gold: #c9a640;
    --gold-deep: #8d6f1e;
    --maroon: #7b2231;
    --text-light: #f1efe8;
    --accent-yellow: #e9cf2b;
    --ornament-gold: #6b5a22;
    --ornament-dark: #3b3212;
  }
  * { margin: 0; padding: 0; box-sizing: border-box; }
  html, body { width: 1200px; height: 871px; overflow: hidden; }
  body {
    background: var(--stage);
    font-family: "Cinzel", "Times New Roman", serif;
    position: relative;
  }

  .card {
    position: absolute;
    width: 620px;
    height: 354px;
    border-radius: 4px;
    overflow: hidden;
    box-shadow: 0 10px 30px rgba(0,0,0,.45);
  }

  /* Front */
  .card--front {
    left: 90px; top: 60px;
    padding: 16px;
    background: linear-gradient(135deg, var(--gold-light), var(--gold) 45%, var(--gold-deep) 75%, var(--gold-light));
  }
  .card--front .face {
    width: 100%; height: 100%;
    background: var(--card-white);
    display: flex; align-items: center; justify-content: center;
  }
  .brand-name {
    color: var(--maroon);
    font-weight: 700;
    letter-spacing: .5px;
    line-height: 1.1;
  }
  .card--front .brand-name { font-size: 40px; text-align: center; }

  /* Back */
  .card--back {
    left: 490px; top: 457px;
    background: var(--card-black);
    border-left: 5px solid var(--gold);
    border-bottom: 6px solid var(--gold);
  }
  .card--back .brand-name {
    position: absolute; left: 54px; top: 40px;
    font-size: 30px;
  }
  .ornament {
    position: absolute;
    right: -30px; bottom: -40px;
    width: 240px; height: 300px;
    border-radius: 50% 50% 18% 18% / 60% 60% 18% 18%;
    background: radial-gradient(ellipse at 50% 50%, var(--ornament-gold), var(--ornament-dark) 80%);
  }
  .person {
    position: absolute; left: 54px; top: 162px;
  }
  .person__name {
    color: var(--text-light);
    font-size: 20px; font-weight: 600; letter-spacing: 1.5px;
    text-transform: uppercase;
  }
  .person__title {
    color: var(--accent-yellow);
    font-size: 12px; letter-spacing: 1px;
    text-transform: uppercase; margin-top: 2px;
  }
  .contact {
    position: absolute; left: 270px; top: 186px;
    color: var(--text-light);
    font-size: 12.5px; letter-spacing: .8px;
    text-transform: uppercase; line-height: 1.5;
  }
  .contact__address { margin-bottom: 16px; }
  .contact__row { display: flex; align-items: center; gap: 12px; font-size: 15px; }
  .contact__row svg { width: 13px; height: 13px; flex: none; }
</style>
</head>
<body>

  <section class="card card--front" aria-label="Business card front">
    <div class="face">
      <p class="brand-name">Bright Harbor<br>Real Estate Co.</p>
    </div>
  </section>

  <section class="card card--back" aria-label="Business card back">
    <div class="ornament" role="img" aria-label="Large gold fleur-de-lis decoration"></div>

    <p class="brand-name">Bright Harbor<br>Real Estate Co.</p>

    <div class="person">
      <p class="person__name">Renata Dubois</p>
      <p class="person__title">Broker/Owner</p>
    </div>

    <div class="contact">
      <p class="contact__address">Office 4172<br>Pelton Rd Belle Ridge LA 70612</p>
      <p class="contact__row">
        <svg viewBox="0 0 16 16" aria-hidden="true"><path fill="var(--gold)" d="M2 5c0-2 2-3 6-3s6 1 6 3v1h-3V5H5v1H2z M4 7h8l2 7H2z"/></svg>
        <span>337-502-4173</span>
      </p>
      <p class="contact__row">
        <svg viewBox="0 0 16 16" aria-hidden="true"><rect x="4" y="1" width="8" height="14" rx="1.5" fill="var(--gold)"/><rect x="5.5" y="3" width="5" height="8" fill="var(--card-black)"/></svg>
        <span>Cell 337-618-9034</span>
      </p>
    </div>
  </section>

</body>
</html>
```